Business Card Design for Consulting Company

I require a Business Card design for my Consulting company. <br/><br/>My company name is: Marek Olvani Consulting Inc.<br/>My website is: www.marekolvaniconsulting.example<br/><br/>My company focuses on management and software development for the Tallobrix CRM platform (www.tallobrix.example)<br/><br/>I have a logo already designed...see attached.
Updates

Also Include my Name and Title: Marek T.L. Olvani President

Target Market(s)

Tallobrix Customers

Contact Information for Business Card

Only include my LOGO (provided)
My Name: Marek TL Olvani
My Title: President
My Company Name: Marek Olvani Consulting Inc.
My Website: www.marekolvaniconsulting.example
My Email: marek.olvani.consulting@mailbox.example

NO PHONE NUMBER
NO ADDRESS

Font styles to use
Serif
Sans Serif
Other font styles liked:
• see my website: www.marekolvaniconsulting.example

Colors

Designer to choose colors to be used in the design.

Requirements
Must have
• Must include my Orange
• Include my name (Marek T.L. Olvani), title (President) company name, website and email
• It should also have a tag line like: Tallobrix Consulting
• I'm flexible with the tag line
Should not have
• Don't include my phone number or address

```html
<!DOCTYPE html>
<html lang="en">
<head>
<meta charset="utf-8">
<title>Marek Olvani Consulting Inc. — Business Card</title>
<link rel="stylesheet" href="https://fonts.googleapis.com/css2?family=Arimo:wght@400;700&family=Saira:wght@500;600&display=swap">
<style>
  :root {
    --brand-orange: #f5861f;
    --card-white: #ffffff;
    --ink-grey: #4a4a4a;
    --backdrop: #2f3238;
    --corner: 96px;
  }
  * { box-sizing: border-box; margin: 0; padding: 0; }
  html, body {
    width: 1200px;
    height: 1000px;
    overflow: hidden;
    background: var(--backdrop);
  }
  .sheet {
    width: 1200px;
    height: 1000px;
    display: flex;
    flex-direction: column;
    align-items: center;
    justify-content: center;
    gap: 56px;
  }
  .card {
    position: relative;
    width: 780px;
    height: 430px;
    border-radius: var(--corner) 0 var(--corner) 0;
    overflow: hidden;
  }

  /* Front */
  .card--front {
    background: var(--brand-orange);
    color: var(--card-white);
    text-align: center;
  }
  .front__mark {
    position: absolute;
    top: 92px;
    left: 0;
    right: 0;
    display: flex;
    align-items: center;
    justify-content: center;
    gap: 18px;
    font-family: "Saira", sans-serif;
    font-weight: 600;
    font-size: 66px;
    line-height: 1;
    letter-spacing: 1px;
  }
  .front__mark-square {
    width: 30px;
    height: 30px;
    background: var(--card-white);
  }
  .front__company {
    position: absolute;
    top: 212px;
    left: 0;
    right: 0;
    font-family: "Saira", sans-serif;
    font-weight: 500;
    font-size: 32px;
    letter-spacing: 1.5px;
  }
  .front__tagline {
    position: absolute;
    top: 340px;
    left: 0;
    right: 0;
    font-family: "Arimo", sans-serif;
    font-size: 19px;
    letter-spacing: 0.5px;
  }

  /* Back */
  .card--back {
    background: var(--card-white);
    color: var(--ink-grey);
    font-family: "Arimo", sans-serif;
  }
  .back__name {
    position: absolute;
    top: 74px;
    left: 72px;
    color: var(--brand-orange);
    font-weight: 700;
    font-size: 34px;
    letter-spacing: 0.5px;
  }
  .back__title {
    position: absolute;
    top: 120px;
    left: 72px;
    font-size: 20px;
  }
  .back__contacts {
    position: absolute;
    top: 262px;
    left: 56px;
    list-style: none;
    display: flex;
    flex-direction: column;
    gap: 12px;
    font-size: 19px;
  }
  .back__contacts li {
    display: flex;
    align-items: center;
    gap: 10px;
  }
  .contact-icon { width: 16px; height: 16px; flex: none; }
  .back__mark {
    position: absolute;
    right: 70px;
    bottom: 96px;
    display: flex;
    align-items: center;
    gap: 12px;
    color: var(--brand-orange);
    font-family: "Arimo", sans-serif;
    font-weight: 700;
    font-size: 34px;
  }
  .back__mark-square {
    width: 22px;
    height: 22px;
    background: var(--brand-orange);
  }
</style>
</head>
<body>
<main class="sheet">
  <section class="card card--front" aria-label="Card front">
    <div class="front__mark">
      <span class="front__mark-square" aria-hidden="true"></span>
      <span>Marek Olvani</span>
    </div>
    <p class="front__company">Marek Olvani Consulting Inc.</p>
    <p class="front__tagline">Tallobrix Consulting</p>
  </section>

  <section class="card card--back" aria-label="Card back">
    <h1 class="back__name">Marek T.L. Olvani</h1>
    <p class="back__title">President</p>
    <ul class="back__contacts">
      <li>
        <svg class="contact-icon" viewBox="0 0 16 16" aria-hidden="true">
          <rect x="1" y="3" width="14" height="10" fill="none" stroke="#f5861f" stroke-width="2"/>
          <path d="M1 3 L8 9 L15 3" fill="none" stroke="#f5861f" stroke-width="2"/>
        </svg>
        <span>marek.olvani.consulting@mailbox.example</span>
      </li>
      <li>
        <svg class="contact-icon" viewBox="0 0 16 16" aria-hidden="true">
          <circle cx="8" cy="8" r="7" fill="#f5861f"/>
          <path d="M1 8 H15 M8 1 C4 5 4 11 8 15 M8 1 C12 5 12 11 8 15" fill="none" stroke="#fff" stroke-width="1.2"/>
        </svg>
        <span>www.marekolvaniconsulting.example</span>
      </li>
    </ul>
    <div class="back__mark">
      <span class="back__mark-square" aria-hidden="true"></span>
      <span>Marek Olvani</span>
    </div>
  </section>
</main>
</body>
</html>
```